Business card design needed

I need a business card for my new Food & Lifestyle Coaching business - "Bloomwell Food & Lifestlye Coaching"

i already have a logo and would like to have that incorporated into the business card, obviously.

i would like a design that says "fresh" and "funky" - my target market is female, aged 20-45 so i want something that will stand out to them when they see it.

My "Company Colour" is Apple Green
Updates

Thankyou to everyone who has submitted a design for my project. At this stage i have quite a large number of designs to chose from and with only a short time until my project closes i am focusing now on chosing from those i have already shortlisted so am unfortunately not considering any new desings.

Thankyou again for your interest in my project.

Target Market(s)

Female, Health Conscious (or looking to improve their health/lifestyle), aged between 20-45

Industry/Entity Type

Business

Contact Information for Business Card

Tessa Harlow
Ph: 0438215790
Email: hellobloom@quarlmail.com

Requirements
Must have
• Must include my existing Logo
Nice to have
• Would be nice to incoirporate and appointment card on the back

```html
<!DOCTYPE html>
<html lang="en">
<head>
<meta charset="utf-8">
<title>Bloomwell Food &amp; Lifestlye Coaching – Business &amp; Appointment Card</title>
<link rel="stylesheet" href="https://fonts.googleapis.com/css2?family=Delius&family=Open+Sans:wght@400&display=swap">
<style>
  :root {
    --backdrop: #2e2e2e;
    --card: #ffffff;
    --apple-green: #7cc242;
    --apple-green-light: #b8e08a;
    --apple-green-deep: #5fa52c;
    --ink: #1a1a1a;
    --label-green: #6db33f;
    --card-shadow: rgba(0,0,0,0.45);
  }
  * { margin: 0; padding: 0; box-sizing: border-box; }
  html, body { width: 1200px; height: 900px; overflow: hidden; }
  body { background: var(--backdrop); position: relative; font-family: "Delius", cursive; }

  .card {
    position: absolute;
    width: 540px;
    height: 310px;
    background: var(--card);
    box-shadow: 0 6px 18px var(--card-shadow);
  }
  .card-frame { position: absolute; inset: 0; }
  .card-frame rect {
    fill: none;
    stroke: var(--apple-green);
    stroke-width: 3;
    stroke-linecap: round;
    stroke-dasharray: 0 7;
  }

  /* Front */
  .card-front { left: 120px; top: 130px; }
  .contact-pill {
    position: absolute;
    right: 20px; top: 28px;
    height: 24px;
    padding: 0 14px;
    border-radius: 12px;
    background: var(--apple-green);
    color: #fff;
    font-family: "Open Sans", Arial, sans-serif;
    font-size: 13px;
    line-height: 24px;
    white-space: nowrap;
  }
  .brand {
    position: absolute;
    left: 0; right: 0; top: 92px;
    text-align: center;
    color: var(--ink);
  }
  .brand-name { font-size: 54px; line-height: 1; }
  .brand-tagline { font-size: 15px; margin-top: 6px; }
  .person-name {
    position: absolute;
    left: 0; right: 0; top: 232px;
    text-align: center;
    font-size: 24px;
    color: var(--ink);
  }
  .corner-art {
    position: absolute;
    right: 14px; top: 196px;
    width: 72px; height: 62px;
    border-radius: 10px;
    background: radial-gradient(circle at 40% 35%, var(--apple-green-light), var(--apple-green));
  }

  /* Back */
  .card-back { left: 540px; top: 460px; }
  .appointment-title {
    position: absolute;
    left: 58px; top: 66px;
    font-size: 26px;
    font-weight: 400;
    color: var(--ink);
  }
  .appointment-fields {
    position: absolute;
    left: 58px; top: 118px;
    width: 250px;
    list-style: none;
    font-family: "Open Sans", Arial, sans-serif;
    font-size: 13px;
    color: var(--label-green);
  }
  .appointment-fields li {
    display: flex;
    align-items: flex-end;
    height: 30px;
  }
  .appointment-fields .field-line {
    flex: 1;
    margin-left: 6px;
    margin-bottom: 4px;
    border-bottom: 1.5px solid var(--apple-green);
  }
  .feature-art {
    position: absolute;
    left: 300px; top: 14px;
    width: 200px; height: 190px;
    border-radius: 18px;
    background: radial-gradient(circle at 45% 40%, var(--apple-green-light), var(--apple-green) 60%, var(--apple-green-deep));
  }
</style>
</head>
<body>

  <section class="card card-front" aria-label="Business card front">
    <svg class="card-frame" width="540" height="310" viewBox="0 0 540 310" aria-hidden="true">
      <rect x="30" y="40" width="480" height="240" rx="22" ry="22"/>
    </svg>
    <div class="contact-pill">0438215790 | hellobloom@quarlmail.com</div>
    <div class="brand">
      <div class="brand-name">Bloomwell</div>
      <div class="brand-tagline">Food &amp; Lifestlye Coaching</div>
    </div>
    <div class="person-name">Tessa Harlow</div>
    <div class="corner-art" role="img" aria-label="Small green leaf decoration"></div>
  </section>

  <section class="card card-back" aria-label="Appointment card back">
    <svg class="card-frame" width="540" height="310" viewBox="0 0 540 310" aria-hidden="true">
      <rect x="30" y="40" width="480" height="240" rx="22" ry="22"/>
    </svg>
    <div class="feature-art" role="img" aria-label="Large glossy green leaf illustration"></div>
    <h2 class="appointment-title">Appointment</h2>
    <ul class="appointment-fields">
      <li>Date:<span class="field-line"></span></li>
      <li>Time:<span class="field-line"></span></li>
      <li>Date:<span class="field-line"></span></li>
      <li>Time:<span class="field-line"></span></li>
    </ul>
  </section>

</body>
</html>
```